Corvane Electrical Solutions

On one side. LOGO (underneath:) Commercial Industrial Residential

- NAME & CONTACT DETAILS

Marcus T. Hollings
Project Manager

(Cell icon) (441) 582-6197
(Email icon) cvnelectricalsoultions@mailventra.com
(Facebook & Instagram icons )@cvnelectricalsolutions

Other side: LOGO - underneath ELECTRICAL CONSTRUCTION & MAINTENANCE . LED LIGHTING & AUTOMATION . LIFE SAFETY SYSTEMS (FIRE ALARM / SECURITY) . DATA & COMMUNICATION

```html
<!DOCTYPE html>
<html lang="en">
<head>
<meta charset="utf-8">
<title>Corvane Electrical Solutions – Business Card</title>
<link rel="stylesheet" href="https://fonts.googleapis.com/css2?family=Montserrat:wght@400;500;600;700&display=swap">
<style>
  :root {
    --teal: #10566c;
    --ink: #2b2b2b;
    --grey: #444446;
    --paper: #ffffff;
    --backdrop: #232325;
  }
  * { margin: 0; padding: 0; box-sizing: border-box; }
  html, body {
    width: 1200px; height: 1200px; overflow: hidden;
    background: var(--backdrop);
    font-family: "Montserrat", sans-serif;
  }
  .card {
    position: absolute;
    box-shadow: 0 14px 30px rgba(0,0,0,.45);
  }

  /* Front: services */
  .card-front {
    left: 292px; top: 220px; width: 599px; height: 359px;
    background: var(--teal); color: var(--paper);
  }
  .services {
    position: absolute; left: 50px; top: 146px;
    list-style: none;
    font-size: 11.5px; font-weight: 500; line-height: 18px;
  }
  .services li::before {
    content: ""; display: inline-block;
    width: 4px; height: 4px; border-radius: 50%;
    background: var(--paper); margin: 0 6px 2px 0; vertical-align: middle;
  }
  .brand-vertical {
    position: absolute; left: 488px; top: 208px;
    transform: rotate(-90deg); transform-origin: 0 0;
    width: 190px;
    font-size: 15px; font-weight: 500; letter-spacing: 3px; line-height: 19px;
    color: var(--paper); text-transform: uppercase;
  }

  /* Back: contact */
  .card-back {
    left: 287px; top: 630px; width: 609px; height: 365px;
    background: var(--paper);
  }
  .brand {
    position: absolute; left: 47px; top: 34px;
    font-size: 19px; font-weight: 600; letter-spacing: 4px; line-height: 22px;
    color: var(--teal); text-transform: uppercase;
  }
  .sectors {
    position: absolute; left: 47px; top: 112px;
    font-size: 9.5px; font-weight: 500; letter-spacing: 2.6px;
    color: var(--ink);
  }
  .sectors .sep { color: var(--teal); margin: 0 4px 0 2px; }
  .person { position: absolute; left: 46px; top: 244px; }
  .person-name {
    font-size: 16.5px; font-weight: 700; color: var(--teal);
    letter-spacing: .2px;
  }
  .person-role { font-size: 11.5px; font-weight: 500; color: var(--grey); margin-top: 1px; }
  .person-rule { width: 50px; height: 2px; background: var(--teal); margin-top: 10px; }
  .contact {
    position: absolute; left: 46px; top: 300px;
    list-style: none; font-size: 12.5px; color: var(--grey); line-height: 19.5px;
  }
  .contact li, .social { display: flex; align-items: center; gap: 4px; }
  .icon { width: 12px; height: 12px; flex: none; }
  .social {
    position: absolute; left: 378px; top: 319.5px;
    font-size: 12.5px; color: var(--grey); line-height: 19.5px;
  }
  .social .dot {
    width: 12px; height: 12px; border-radius: 50%;
    border: 1px solid var(--teal); margin-right: 2px;
  }
</style>
</head>
<body>

<section class="card card-front">
  <ul class="services">
    <li>ELECTRICAL CONSTRUCTION &amp; MAINTENANCE</li>
    <li>LED LIGHTING &amp; AUTOMATION</li>
    <li>LIFE SAFETY SYSTEMS (FIRE ALARM / SECURITY)</li>
    <li>DATA &amp; COMMUNICATION</li>
  </ul>
  <div class="brand-vertical">Corvane<br>Electrical<br>Solutions</div>
</section>

<section class="card card-back">
  <div class="brand">Corvane<br>Electrical<br>Solutions</div>
  <div class="sectors">COMMERCIAL<span class="sep"> | </span>INDUSTRIAL<span class="sep"> | </span>RESIDENTIAL</div>

  <div class="person">
    <div class="person-name">MARCUS T. HOLLINGS</div>
    <div class="person-role">Project Manager</div>
    <div class="person-rule"></div>
  </div>

  <ul class="contact">
    <li>
      <svg class="icon" viewBox="0 0 12 12" aria-hidden="true">
        <circle cx="6" cy="6" r="5.4" fill="none" stroke="#10566c" stroke-width="1"/>
        <path d="M4 3.2 L5 3 L5.6 4.5 L4.9 5 Q5.5 6.5 7 7.1 L7.5 6.4 L9 7 L8.8 8 Q6.5 8.6 4.7 6.8 Q3.3 5.2 4 3.2Z" fill="#10566c"/>
      </svg>
      (441) 582-6197
    </li>
    <li>
      <svg class="icon" viewBox="0 0 12 12" aria-hidden="true">
        <circle cx="6" cy="6" r="5.4" fill="none" stroke="#10566c" stroke-width="1"/>
        <rect x="3.3" y="4" width="5.4" height="4" fill="none" stroke="#10566c" stroke-width=".9"/>
        <path d="M3.3 4 L6 6.2 L8.7 4" fill="none" stroke="#10566c" stroke-width=".9"/>
      </svg>
      cvnelectricalsoultions@mailventra.com
    </li>
  </ul>

  <div class="social"><span class="dot"></span>@cvnelectricalsolutions</div>
</section>

</body>
</html>
```